Maple Jubilee 2017 Poster

We need a poster design for our private school's annual Maple Jubilee. We're a progressive school in nyc, with deep community roots and a rich hundred year history. The community cherishes the events and looks forward to seeing what excitement each new year will bring! The posters will be displayed thoughout the school, appealing to a diverse audience of children and their' families.
We'd like a vintage vibe, circa turn of the 20th century (1900s). Please reference the images I've included, which give some inspiration. Also, as pertains to the theme, I'd like a representation of a vintage apple basket, brimming with apples, but with a planet earth nestled inside as the main focal point. Kind of like a words fair meets the harvest...
Also typography should be semi old fashioned looking as well.
COPY - Should Include the following:

Brook & Meadow
Maple Jubilee of Peoples

October 14th 12:00-4:00pm
Celebrate an Afternoon of Great Food, Music, Entertainment, & Fun

Tickets will be available for sale at Pickup

Target Market(s)

School Community, children and their parents, faculty, etc.

Industry/Entity Type

School

Font styles to use
Other font styles liked:
• Something old world fair, country looking

Colors
ec1f27
fcca95
ffcf3e

Requirements
Must have
• We'd like a vintage vibe, circa turn of the 20th century (1900s). Please reference the images I've included, which give some inspiration. Also, as pertains to the theme, I'd like a representation of a vintage apple basket, brimming with apples, but with a planet earth nestled inside as the main focal point. Kind of like a words fair meets the harvest...
• Also typography should be semi old fashioned looking as well.
• COPY - Should Include the following:
• Brook & Meadow
• Maple Jubilee of Peoples
• October 14th 12:00-4:00pm
• Celebrate an Afternoon of Great Food, Music, Entertainment, & Fun
• Tickets will be available for sale at Pickup
Nice to have
• Attractive design, draws you in, gets you interested in the event, informs you of important details.
Should not have
• I think that the design ask is pretty straight forward.

```html
<!DOCTYPE html>
<html lang="en">
<head>
<meta charset="utf-8">
<title>Maple Jubilee of Peoples</title>
<link href="https://fonts.googleapis.com/css2?family=Lobster&family=Rye&family=Bebas+Neue&family=Arimo:wght@700&display=swap" rel="stylesheet">
<style>
  :root {
    --plum: #2f1f30;
    --ink: #3a2238;
    --coral: #f26a4e;
    --gold: #fbb846;
    --ribbon: #fcc04e;
    --scene-top: #f5cfc8;
    --scene-mid: #f3b89a;
    --scene-low: #f1a56c;
    --focal-top: #eeb0a0;
    --focal-low: #e99a6a;
    --note: #f7c04a;
  }
  html, body { margin: 0; padding: 0; overflow: hidden; }
  body { width: 900px; height: 1200px; background: var(--plum); }
  .poster { position: relative; width: 900px; height: 1200px; overflow: hidden; background: var(--plum); }
  .frame { position: absolute; left: 0; top: 0; width: 900px; height: 1080px; }
  .ribbon { position: absolute; background: var(--ribbon); color: var(--ink); text-align: center; }
  .host-ribbon {
    left: 216px; top: 194px; width: 468px; height: 52px;
    clip-path: polygon(0 0, 100% 0, 96% 50%, 100% 100%, 0 100%, 4% 50%);
    font: 38px/56px "Rye", serif; letter-spacing: 1px;
  }
  .event-title {
    position: absolute; left: 0; width: 900px; top: 240px; margin: 0;
    text-align: center; color: var(--ink); font-weight: 400;
    font: 104px/1 "Lobster", cursive; letter-spacing: 1px;
  }
  .event-sub {
    position: absolute; left: 0; width: 900px; top: 350px;
    text-align: center; color: var(--ink);
    font: 60px/1 "Rye", serif; letter-spacing: 2px;
  }
  .date-ribbon {
    left: 210px; top: 720px; width: 492px; height: 138px;
    clip-path: polygon(0 0, 100% 0, 94% 50%, 100% 100%, 0 100%, 6% 50%);
    font-family: "Bebas Neue", sans-serif;
  }
  .date-ribbon .day { display: block; font-size: 82px; line-height: 70px; margin-top: 6px; }
  .date-ribbon .time { display: block; font-size: 78px; line-height: 62px; }
  .details {
    position: absolute; left: 0; width: 900px; top: 1068px;
    text-align: center; color: var(--note); font-family: "Arimo", Arial, sans-serif; font-weight: 700;
  }
  .details p { margin: 0; }
  .details .lead { font-size: 21px; line-height: 32px; }
  .details .tickets { font-size: 27px; line-height: 40px; }
</style>
</head>
<body>
<div class="poster">
  <svg class="frame" viewBox="0 0 900 1080" xmlns="http://www.w3.org/2000/svg">
    <defs>
      <linearGradient id="sceneTone" x1="0" y1="0" x2="0" y2="1">
        <stop offset="0" stop-color="var(--scene-top)"/>
        <stop offset="0.45" stop-color="var(--scene-mid)"/>
        <stop offset="1" stop-color="var(--scene-low)"/>
      </linearGradient>
      <linearGradient id="focalTone" x1="0" y1="0" x2="0" y2="1">
        <stop offset="0" stop-color="var(--focal-top)"/>
        <stop offset="1" stop-color="var(--focal-low)"/>
      </linearGradient>
      <path id="frameShape" d="M160 40 L420 40 Q450 20 480 40 L740 40 C760 62 790 90 820 96 Q808 540 820 980 C790 986 760 1012 740 1030 L480 1030 Q450 1050 420 1030 L160 1030 C140 1012 110 986 80 980 Q92 540 80 96 C110 90 140 62 160 40 Z"/>
    </defs>
    <use href="#frameShape" fill="none" stroke="var(--coral)" stroke-width="58" stroke-linejoin="round"/>
    <use href="#frameShape" fill="none" stroke="var(--gold)" stroke-width="42" stroke-linejoin="round"/>
    <use href="#frameShape" fill="none" stroke="var(--coral)" stroke-width="14" stroke-linejoin="round"/>
    <use href="#frameShape" fill="url(#sceneTone)" role="img" aria-label="Photo of bare autumn trees and long shadows across a lawn"/>
    <rect class="focal-area" x="140" y="420" width="620" height="280" rx="18" fill="url(#focalTone)" opacity="0.85" role="img" aria-label="Photo of a two-storey house with a long balcony, set behind bare tree trunks"/>
  </svg>

  <div class="ribbon host-ribbon">BROOK &amp; MEADOW</div>
  <h1 class="event-title">Maple Jubilee</h1>
  <div class="event-sub">OF PEOPLES</div>

  <div class="ribbon date-ribbon">
    <span class="day">OCTOBER 14TH</span>
    <span class="time">12:00-4:00PM</span>
  </div>

  <div class="details">
    <p class="lead">Celebrate an Afternoon of Great Food, Music, Entertainment, &amp; Fun</p>
    <p class="tickets">Tickets will be available for sale at Pickup</p>
  </div>
</div>
</body>
</html>
```